Automotive Accessories Business Card

Design a business template that match our new logo design and our industry.

https://www.kelvramotive.com/

Target Market(s)

Aftermarket auto parts and accessories

Industry/Entity Type

automotive

Contact Information for Business Card

company logo

Font styles to use
Serif
Sans Serif

Colors
EB3D1F
EC4F4E
F09395
F8D3D4
FCEDEE

```html
<!DOCTYPE html>
<html lang="en">
<head>
<meta charset="utf-8">
<title>Kelvra Motive Business Card</title>
<link rel="stylesheet" href="https://fonts.googleapis.com/css2?family=Arimo:wght@400;700&display=swap">
<style>
  :root {
    --bg: #e9e9ea;
    --red: #d82027;
    --ink: #3d3d3f;
    --soft: #58595b;
    --white: #ffffff;
  }
  * { margin: 0; padding: 0; box-sizing: border-box; }
  html, body { width: 1200px; height: 1015px; overflow: hidden; }
  body {
    background: var(--bg);
    font-family: "Arimo", Arial, sans-serif;
    position: relative;
  }
  .card {
    position: absolute;
    left: 250px;
    width: 700px;
    height: 400px;
    overflow: hidden;
    box-shadow: 0 6px 18px rgba(0,0,0,.18);
  }
  .card-front { top: 70px; background: var(--red); }
  .card-back  { top: 530px; background: var(--white); }

  .front-brand {
    position: absolute;
    left: 0; right: 0; top: 165px;
    text-align: center;
    color: var(--white);
    font-weight: 700;
    font-size: 40px;
    letter-spacing: 2px;
  }
  .front-brand .mark {
    display: inline-block;
    width: 22px; height: 22px;
    background: var(--white);
    margin-right: 14px;
    vertical-align: 2px;
  }
  .front-strip {
    position: absolute;
    left: 0; right: 0; bottom: 12px;
    height: 22px;
    background: linear-gradient(90deg, #f2b8ba, #ffffff 50%, #f2b8ba);
    opacity: .85;
  }

  .back-brand {
    position: absolute;
    right: 60px; top: 60px;
    color: var(--red);
    font-weight: 700;
    font-size: 30px;
    letter-spacing: 1.5px;
  }
  .back-brand .mark {
    display: inline-block;
    width: 16px; height: 16px;
    background: var(--red);
    margin-right: 10px;
    vertical-align: 2px;
  }
  .person { position: absolute; left: 48px; top: 150px; }
  .person-name {
    color: var(--red);
    font-weight: 700;
    font-size: 26px;
    letter-spacing: .5px;
  }
  .person-role { color: var(--ink); font-size: 20px; margin-top: 2px; }

  .contact { position: absolute; left: 48px; bottom: 72px; color: var(--ink); font-size: 20px; line-height: 1.4; }
  .contact-line { display: flex; align-items: center; gap: 10px; }
  .contact-line svg { width: 18px; height: 18px; flex: none; }

  .address {
    position: absolute;
    right: 60px; top: 190px;
    text-align: right;
    color: var(--ink);
    font-size: 19px;
    line-height: 1.3;
  }
  .web-band {
    position: absolute;
    right: 0; bottom: 0;
    width: 330px; height: 58px;
    background: var(--ink);
    color: var(--white);
    font-size: 19px;
    letter-spacing: .8px;
    display: flex; align-items: center; justify-content: flex-end;
    padding-right: 40px;
  }
  .back-strip {
    position: absolute;
    left: 0; bottom: 0;
    width: 370px; height: 26px;
    background: linear-gradient(90deg, var(--ink), var(--red));
    opacity: .9;
  }
</style>
</head>
<body>
  <section class="card card-front">
    <div class="front-brand"><span class="mark"></span>KELVRA MOTIVE</div>
    <div class="front-strip" role="img" aria-label="Checkered racing flag strip"></div>
  </section>

  <section class="card card-back">
    <div class="back-brand"><span class="mark"></span>KELVRA MOTIVE</div>

    <div class="person">
      <div class="person-name">DANIEL MERCER</div>
      <div class="person-role">Managing Director</div>
    </div>

    <div class="address">
      421, Address line goes here<br>45452, Country Name
    </div>

    <div class="contact">
      <div class="contact-line">
        <svg viewBox="0 0 24 24" aria-hidden="true"><path fill="#d82027" d="M6.6 10.8a15.1 15.1 0 0 0 6.6 6.6l2.2-2.2a1 1 0 0 1 1-.25 11.4 11.4 0 0 0 3.6.57 1 1 0 0 1 1 1V20a1 1 0 0 1-1 1A17 17 0 0 1 3 4a1 1 0 0 1 1-1h3.5a1 1 0 0 1 1 1c0 1.25.2 2.45.57 3.57a1 1 0 0 1-.25 1z"/></svg>
        <span>044-555 010 246</span>
      </div>
      <div class="contact-line">
        <svg viewBox="0 0 24 24" aria-hidden="true"><path fill="#d82027" d="M2 5h20v14H2z"/><path fill="none" stroke="#fff" stroke-width="1.6" d="M2.5 5.5 12 13l9.5-7.5"/></svg>
        <span>info@kelvramotive.com</span>
      </div>
    </div>

    <div class="back-strip" role="img" aria-label="Checkered racing flag strip"></div>
    <div class="web-band">www.kelvramotive.com</div>
  </section>
</body>
</html>
```